Brightstone Roofing Business Card

This is my current business card. But I’d like to make some changes. Somewhere on the card I’d like to list some of the services we offer. Maybe on the back? But I’d still like to keep the red. White and black modern look.

-residential & commercial roofing
-Roof Repairs & Maintenance
-Storm Damage & Insurance Claims specialist
-Christmas Lights and permanent Christmas lights
Fencing. Windows. Gutters. Siding. Sheetrock, painting.

```html
<!DOCTYPE html>
<html lang="en">
<head>
<meta charset="utf-8">
<title>Brightstone Roofing Business Card</title>
<link href="https://fonts.googleapis.com/css2?family=Audiowide&family=Open+Sans:wght@400;600&family=PT+Sans+Narrow:wght@400;700&display=swap" rel="stylesheet">
<style>
  :root {
    --backdrop: #d4d5d7;
    --red: #e0262b;
    --red-deep: #7a0f12;
    --red-dark: #5c0a0c;
    --black: #121212;
    --white: #ffffff;
    --soft-white: #f2f2f2;
  }
  * { margin: 0; padding: 0; box-sizing: border-box; }
  html, body { width: 900px; height: 1200px; overflow: hidden; }
  body { background: var(--backdrop); position: relative; font-family: "Open Sans", sans-serif; }

  .card { position: absolute; left: 136px; width: 630px; height: 357px; border-radius: 11px; overflow: hidden; }

  /* front */
  .card-front { top: 215px; }
  .tartan-field {
    position: absolute; inset: 0;
    background:
      linear-gradient(180deg, transparent 0 27%, rgba(255,255,255,.18) 27% 33%, transparent 33% 44%, rgba(0,0,0,.55) 44% 66%, transparent 66%),
      linear-gradient(90deg, var(--red-deep) 0%, var(--red) 20%, var(--red-deep) 45%, var(--red) 70%, var(--red-deep) 100%);
  }
  .front-mark { position: absolute; left: 50%; top: 71px; width: 142px; height: 142px; margin-left: -71px; border-radius: 50%; background: var(--black); border: 4px solid var(--white); }
  .front-name {
    position: absolute; left: 0; right: 0; top: 226px; text-align: center;
    font-family: "Audiowide", sans-serif; color: var(--white); font-size: 30px; line-height: 36px; letter-spacing: 1px;
  }

  /* back */
  .card-back { top: 629px; background: var(--black); }
  .back-brand { position: absolute; left: 60px; top: 48px; width: 226px; text-align: center; }
  .back-mark { width: 92px; height: 92px; margin: 0 auto 14px; border-radius: 50%; background: var(--red); border: 3px solid var(--white); }
  .back-name { font-family: "Audiowide", sans-serif; color: var(--white); font-size: 19px; line-height: 24px; letter-spacing: .5px; }

  .divider { position: absolute; left: 296px; top: 57px; width: 1px; height: 135px; background: var(--soft-white); }

  .contact { position: absolute; left: 324px; top: 56px; color: var(--white); }
  .person { font-family: "Audiowide", sans-serif; font-size: 23px; letter-spacing: 1.5px; line-height: 28px; }
  .person .first { color: var(--red); }
  .role { font-size: 14px; letter-spacing: 1.5px; margin-top: 2px; font-weight: 600; }
  .contact-list { list-style: none; margin-top: 12px; }
  .contact-list li { display: flex; align-items: center; gap: 6px; font-size: 15px; letter-spacing: 1px; height: 25px; }
  .contact-list li.phone { letter-spacing: 2.5px; }
  .contact-list svg { width: 15px; height: 15px; fill: var(--red); flex: none; }

  .services { position: absolute; left: 0; right: 0; top: 224px; text-align: center; }
  .services-title { display: flex; align-items: center; justify-content: center; gap: 14px; font-family: "PT Sans Narrow", sans-serif; font-weight: 700; color: var(--red); font-size: 21px; letter-spacing: .5px; }
  .services-title::before, .services-title::after { content: ""; width: 135px; height: 1px; background: var(--soft-white); }
  .services-list { margin-top: 8px; font-family: "PT Sans Narrow", sans-serif; color: var(--white); font-size: 16.5px; line-height: 25px; }
  .sep { color: var(--red); padding: 0 3px; }

  .tartan-band { position: absolute; left: 0; right: 0; bottom: 0; height: 12px; background: linear-gradient(90deg, var(--red-deep), var(--red) 25%, var(--red-dark) 50%, var(--red) 75%, var(--red-deep)); }
</style>
</head>
<body>

<section class="card card-front">
  <div class="tartan-field" role="img" aria-label="Red, black and white tartan plaid pattern"></div>
  <div class="front-mark"></div>
  <div class="front-name">BRIGHTSTONE<br>ROOFING CO.</div>
</section>

<section class="card card-back">
  <div class="back-brand">
    <div class="back-mark"></div>
    <div class="back-name">BRIGHTSTONE<br>ROOFING CO.</div>
  </div>

  <div class="divider"></div>

  <div class="contact">
    <div class="person"><span class="first">GRANT</span> MERCER</div>
    <div class="role">OWNER</div>
    <ul class="contact-list">
      <li class="phone">
        <svg viewBox="0 0 24 24" aria-hidden="true"><path d="M6.6 10.8a15.1 15.1 0 0 0 6.6 6.6l2.2-2.2a1 1 0 0 1 1-.25 11.4 11.4 0 0 0 3.6.57 1 1 0 0 1 1 1V20a1 1 0 0 1-1 1A17 17 0 0 1 3 4a1 1 0 0 1 1-1h3.5a1 1 0 0 1 1 1c0 1.25.2 2.45.57 3.57a1 1 0 0 1-.25 1z"/></svg>
        682-555-0148
      </li>
      <li>
        <svg viewBox="0 0 24 24" aria-hidden="true"><path d="M2 5h20v14H2z M3.5 6.5 12 13l8.5-6.5" stroke="#121212" stroke-width="1.5"/></svg>
        Grant@brightstoneroofing.co
      </li>
      <li>
        <svg viewBox="0 0 24 24" aria-hidden="true"><path d="M12 2a10 10 0 1 0 0 20 10 10 0 0 0 0-20zm0 2c.9 1.2 1.6 2.6 2 4h-4c.4-1.4 1.1-2.8 2-4zM4.3 14a8 8 0 0 1 0-4h3.4a16 16 0 0 0 0 4zm.9 2h2.9c.3 1.3.8 2.5 1.5 3.6A8 8 0 0 1 5.2 16zm2.9-8H5.2a8 8 0 0 1 4.4-3.6C8.9 5.5 8.4 6.7 8.1 8zM12 20c-.9-1.2-1.6-2.6-2-4h4c-.4 1.4-1.1 2.8-2 4zm2.3-6H9.7a14 14 0 0 1 0-4h4.6a14 14 0 0 1 0 4zm.1 5.6c.7-1.1 1.2-2.3 1.5-3.6h2.9a8 8 0 0 1-4.4 3.6zM16.3 14a16 16 0 0 0 0-4h3.4a8 8 0 0 1 0 4zm-.4-6c-.3-1.3-.8-2.5-1.5-3.6A8 8 0 0 1 18.8 8z"/></svg>
        www.brightstoneroofing.co
      </li>
    </ul>
  </div>

  <div class="services">
    <h2 class="services-title">SERVICES WE OFFER</h2>
    <p class="services-list">
      Residential &amp; Commercial Roofing<span class="sep">|</span>Roof Repairs &amp; Maintenance<br>
      Storm Damage &amp; Insurance Claims specialist<span class="sep">|</span>Christmas Lights and permanent Christmas lights<br>
      Fencing<span class="sep">|</span>Windows<span class="sep">|</span>Gutters<span class="sep">|</span>Siding<span class="sep">|</span>Sheetrock<span class="sep">|</span>Painting.
    </p>
  </div>

  <div class="tartan-band" role="img" aria-label="Thin strip of red, black and white tartan plaid"></div>
</section>

</body>
</html>
```